ORVILMA card Technical Architecture

Hello everyone ORVILMA: It is a consulting firm in Architecture and Construction. I require a card duplexing, sober, elegant, classic but not boring. Update 1: Use the following data for the card. Name: Rodrigo Salinas Tomás Quevedo Position: COO Twitter: @orvilmaAT Homepage: orvilma.com home address not include the participation of all thank you.

Target Market(s)

Construction companies, Architects and Consulting Engineers

Industry/Entity Type

Consulting

Contact Information for Business Card

Los campos que debe tener:
Nombre, Cargo, email, homepage y twitter

Font styles to use
Serif
Sans Serif
Other font styles liked:
• Me gustan playfair display, open sans y roboto, pero estoy sujeto a sus propuestas

Requirements
Must have
• Colors: Present combined proposals in white, red, gray and black Update 1: The two names must be clearly differentiated from the two surnames
Nice to have
• They are free to present their best proposals. I will bring them immediate feedback to the extent you can go see their designs. Complete data for card and logo files will give the winner the

```html
<!DOCTYPE html>
<html lang="es">
<head>
<meta charset="utf-8">
<title>ORVILMA – Business Card</title>
<link rel="stylesheet" href="https://fonts.googleapis.com/css2?family=Roboto:wght@300;400&display=swap">
<style>
  :root {
    --backdrop: #3b3b3d;
    --card: #2a2a2b;
    --ink: #f2f2f2;
    --ink-soft: #b9b9b9;
    --rule: #8a8a8a;
    --accent: #d41f26;
  }
  * { margin: 0; padding: 0; box-sizing: border-box; }
  html, body { width: 900px; height: 1200px; overflow: hidden; }
  body {
    background: var(--backdrop);
    font-family: "Roboto", Arial, sans-serif;
    color: var(--ink);
  }
  .sheet {
    width: 900px; height: 1200px;
    display: grid;
    grid-template-rows: 600px 600px;
    place-items: center;
  }
  .card {
    width: 540px; height: 310px;
    background: var(--card);
    box-shadow: 0 18px 40px rgba(0,0,0,.35);
    position: relative;
  }

  /* Back: contact side */
  .card--contact {
    display: grid;
    grid-template-columns: 230px 1px 1fr;
    align-items: center;
  }
  .brand-block {
    display: flex; align-items: center; justify-content: center; gap: 12px;
  }
  .brand-block .brand-square {
    width: 22px; height: 22px; background: var(--ink);
  }
  .brand-block .brand-name {
    font-weight: 300; font-size: 30px; letter-spacing: 6px; color: var(--ink);
  }
  .divider { width: 1px; height: 190px; background: var(--rule); }
  .contact { padding-left: 30px; }
  .person-name {
    font-weight: 400; font-size: 17px; line-height: 1.25; color: var(--ink);
  }
  .person-role {
    font-weight: 300; font-size: 10px; margin-top: 4px; color: var(--ink-soft);
  }
  .contact-list { list-style: none; margin-top: 22px; }
  .contact-list li {
    display: flex; align-items: center; gap: 8px;
    font-weight: 300; font-size: 13px; line-height: 1.55; color: var(--ink);
  }
  .contact-icon {
    width: 11px; height: 11px; background: var(--accent);
    display: inline-flex; align-items: center; justify-content: center;
    flex: none;
  }

  /* Front: brand side */
  .card--brand {
    display: flex; flex-direction: column; align-items: center; justify-content: center;
  }
  .brand-mark {
    width: 30px; height: 30px; background: var(--accent); margin-bottom: 14px;
  }
  .brand-wordmark {
    font-weight: 300; font-size: 40px; letter-spacing: 14px; color: var(--ink);
    padding-left: 14px;
  }
  .brand-tagline {
    font-weight: 300; font-size: 11px; letter-spacing: 6px; color: var(--ink-soft);
    margin-top: 6px; padding-left: 6px;
  }
</style>
</head>
<body>
<main class="sheet">

  <section class="card card--contact" aria-label="Card back with contact details">
    <div class="brand-block">
      <span class="brand-square"></span>
      <span class="brand-name">ORVILMA</span>
    </div>
    <div class="divider"></div>
    <div class="contact">
      <p class="person-name">Rodrigo Salinas<br>Tomás Quevedo</p>
      <p class="person-role">Director of Operations</p>
      <ul class="contact-list">
        <li>
          <span class="contact-icon">
            <svg width="8" height="8" viewBox="0 0 8 8"><path d="M1.5 0.8 L2.8 0.8 L3.3 2.4 L2.5 3 Q3.2 4.6 5 5.5 L5.6 4.7 L7.2 5.2 L7.2 6.5 Q3.8 7 1 2.4 Z" fill="#fff"/></svg>
          </span>
          0312-5550-1847
        </li>
        <li><span class="contact-icon"></span>@orvilmaAT</li>
        <li><span class="contact-icon"></span>www.orvilma.com</li>
      </ul>
    </div>
  </section>

  <section class="card card--brand" aria-label="Card front with brand name">
    <span class="brand-mark"></span>
    <span class="brand-wordmark">ORVILMA</span>
    <span class="brand-tagline">ARQUITECTURA TÉCNIC</span>
  </section>

</main>
</body>
</html>
```